Industrial Professional Business Card Design (Vantrel Systems)

Would like professional looking business cards. Not too busy leaning towards minimal. Should have a slogan like:
"Industrial Automation and Control".

We are a tech company that programs industrial PLC computers. We also develop custom hardware solutions. Please use the logo for inspiration.

Target Market(s)

Mining, industrial, processing, automation, factory

Industry/Entity Type

Engineering

Contact Information for Business Card

Name, phone, email, website. job title.

Font styles to use
Other font styles liked:
• droid sans

Requirements
Must have
• Use colours that go well with the logo. Not too busy design.

```html
<!DOCTYPE html>
<html lang="en">
<head>
<meta charset="utf-8">
<title>Vantrel Systems — Business Card</title>
<link rel="stylesheet" href="https://fonts.googleapis.com/css2?family=Open+Sans:wght@400;600;700&display=swap">
<style>
  :root {
    --navy: #1c3f6e;
    --navy-deep: #152a5a;
    --steel: #2474a0;
    --orange: #f26722;
    --ink: #1a1a1a;
    --paper: #fcfbfd;
    --backdrop: #e4e5e8;
  }
  * { margin: 0; padding: 0; box-sizing: border-box; }
  html, body {
    width: 1200px;
    height: 900px;
    overflow: hidden;
    background: var(--backdrop);
    font-family: "Open Sans", sans-serif;
  }
  .canvas {
    width: 1200px;
    height: 900px;
    display: flex;
    align-items: center;
    justify-content: center;
  }
  .card {
    position: relative;
    width: 1050px;
    height: 600px;
    background: var(--paper);
    box-shadow: 0 6px 24px rgba(0, 0, 0, 0.18);
    overflow: hidden;
  }
  .wordmark {
    position: absolute;
    left: 64px;
    top: 48px;
    font-size: 74px;
    font-weight: 400;
    letter-spacing: 1px;
    color: var(--navy);
    line-height: 1;
  }
  .slogan {
    position: absolute;
    left: 70px;
    top: 140px;
    font-size: 21px;
    font-weight: 600;
    letter-spacing: 2px;
    text-transform: uppercase;
    color: var(--orange);
  }
  .identity {
    position: absolute;
    left: 70px;
    top: 222px;
  }
  .identity .name {
    font-size: 40px;
    font-weight: 700;
    color: var(--navy-deep);
    line-height: 1.05;
  }
  .identity .role {
    font-size: 23px;
    font-weight: 400;
    color: var(--ink);
    margin-top: 2px;
  }
  .contact {
    position: absolute;
    left: 70px;
    top: 380px;
    list-style: none;
  }
  .contact li {
    display: flex;
    align-items: center;
    gap: 18px;
    font-size: 22px;
    color: var(--ink);
    height: 38px;
  }
  .contact svg {
    width: 24px;
    height: 22px;
    flex: none;
  }
  .brand-disc {
    position: absolute;
    right: 70px;
    top: 150px;
    width: 390px;
    height: 390px;
    border-radius: 50%;
    background: linear-gradient(225deg, var(--navy-deep), var(--steel));
  }
</style>
</head>
<body>
<main class="canvas">
  <article class="card">
    <h1 class="wordmark">Vantrel Systems</h1>
    <p class="slogan">Industrial Automation and Control</p>

    <div class="identity">
      <p class="name">Marcus Hale</p>
      <p class="role">President</p>
    </div>

    <ul class="contact">
      <li>
        <svg viewBox="0 0 24 22" aria-hidden="true">
          <path d="M5 2 L9 2 L10.5 7 L8 9 C9.5 12 11.5 14 14.5 15.5 L16.5 13 L21.5 14.5 L21.5 18.5 C21.5 19.5 20.5 20 19.5 20 C11 19.5 4 12.5 3.5 4 C3.5 3 4 2 5 2 Z" fill="var(--navy)"/>
        </svg>
        +00 000 000 000
      </li>
      <li>
        <svg viewBox="0 0 24 22" aria-hidden="true">
          <rect x="1.5" y="4" width="21" height="14" fill="none" stroke="var(--navy)" stroke-width="1.6"/>
          <path d="M1.5 4 L12 12.5 L22.5 4 M1.5 18 L9 11 M22.5 18 L15 11" fill="none" stroke="var(--navy)" stroke-width="1.6"/>
        </svg>
        info@vantrelsystems.com
      </li>
      <li>
        <svg viewBox="0 0 24 22" aria-hidden="true">
          <g fill="none" stroke="var(--navy)" stroke-width="1.5">
            <circle cx="12" cy="11" r="9.5"/>
            <ellipse cx="12" cy="11" rx="4.2" ry="9.5"/>
            <path d="M2.5 11 H21.5 M4 6 H20 M4 16 H20"/>
          </g>
        </svg>
        www.vantrelsystems.com
      </li>
    </ul>

    <div class="brand-disc" aria-hidden="true"></div>
  </article>
</main>
</body>
</html>
```